Parcel Badge Inc. NEED DESIGNS FOR THE HOLIDAY STICKERS

We need 6 designs for the HOLIDAY SET of Parcel Badges. I have attached some imagery that we like as well as the flagship pack of stickers that were also designed by you AWESOME DESIGNERS!! You are not limited to this imagery, it is only to show you what style we like but remember, YOU ARE THE ARTIST! Each design needs to have a "TO: & FROM:" for people to write in their name and the recipients name. We need designs for the following occasions:

1. HALLOWEEN
2. HAPPY HOLIDAYS (THANKSGIVING, CHRISTMAS, WINTER, LEAVES)
3. ST. PATRICK'S DAY
4. "LET'S CELEBRATE" PATRIOTIC THEME (JULY 4TH, VETERANS DAY, MEMORIAL DAY COMBINED)
5. HAPPY NEW YEAR
6. SUMMER THEME GENERIC

***these 6 designs must fit on one of die cut shapes which are included in the brief***

**PLEASE SUBMIT YOUR IDEA FOR AS MANY DESIGNS AS YOU CAN (PREFERABLY ALL 6). WE NEED 6 DESIGNS SO IF 4 OF YOURS ARE GOOD AND 2 OF ANOTHERS ARE GOOD, YOU WOULD WIN 1ST AND THEY WOULD WIN 2ND.

Font styles to use
Serif
Sans Serif
Decorative
Script

Requirements
Must have
• - lines for "to" and "from"
• - must fit on a die cut shape (provided)
• - must be FUN and colorful!!
Nice to have
• color, imagery, fun!

```html
<!DOCTYPE html>
<html lang="en">
<head>
<meta charset="utf-8">
<title>Happy New Year 2017 – Gift Sticker</title>
<link rel="stylesheet" href="https://fonts.googleapis.com/css2?family=Jost:wght@300;400&family=Oswald:wght@500&display=swap">
<style>
  :root {
    --canvas-bg: #f1f1f1;
    --label-black: #221f1f;
    --frame-teal: #13959c;
    --greeting-gold: #e7c26a;
    --digit-teal: #1fb8bf;
    --digit-coral: #ee3a4f;
    --digit-gold: #f5c451;
    --digit-red: #e8232a;
    --tag-cream: #f7d796;
    --tag-ink: #231f20;
  }
  html, body {
    margin: 0;
    padding: 0;
    width: 1200px;
    height: 900px;
    overflow: hidden;
    background: var(--canvas-bg);
  }
  .canvas {
    position: relative;
    width: 1200px;
    height: 900px;
    background: radial-gradient(ellipse at center, #ffffff 0%, var(--canvas-bg) 75%);
  }
  .sticker {
    position: absolute;
    left: 0;
    top: 0;
    width: 1200px;
    height: 900px;
  }
  .sticker-shape { fill: var(--label-black); }
  .sticker-frame {
    fill: none;
    stroke: var(--frame-teal);
    stroke-width: 5;
  }
  .fireworks {
    position: absolute;
    left: 560px;
    top: 125px;
    width: 505px;
    height: 320px;
    border-radius: 40%;
    background:
      radial-gradient(circle at 45% 22%, rgba(31,184,191,.55) 0%, rgba(31,184,191,0) 18%),
      radial-gradient(circle at 63% 20%, rgba(238,58,79,.5) 0%, rgba(238,58,79,0) 17%),
      radial-gradient(circle at 18% 45%, rgba(231,194,106,.35) 0%, rgba(231,194,106,0) 18%),
      radial-gradient(circle at 80% 38%, rgba(231,194,106,.4) 0%, rgba(231,194,106,0) 17%),
      radial-gradient(circle at 12% 86%, rgba(231,194,106,.5) 0%, rgba(231,194,106,0) 16%),
      radial-gradient(circle at 88% 80%, rgba(31,184,191,.5) 0%, rgba(31,184,191,0) 17%);
  }
  .greeting {
    position: absolute;
    left: 505px;
    width: 600px;
    text-align: center;
    font-family: "Jost", sans-serif;
    font-weight: 300;
    color: var(--greeting-gold);
    line-height: 1;
    margin: 0;
  }
  .greeting-happy { top: 320px; font-size: 42px; letter-spacing: 1px; }
  .greeting-year { top: 368px; font-size: 46px; letter-spacing: 1px; }
  .year-number {
    position: absolute;
    left: 505px;
    top: 388px;
    width: 600px;
    text-align: center;
    font-family: "Oswald", sans-serif;
    font-weight: 500;
    font-size: 280px;
    line-height: 1;
    letter-spacing: -4px;
    margin: 0;
  }
  .digit-teal { color: var(--digit-teal); }
  .digit-coral { color: var(--digit-coral); }
  .digit-gold { color: var(--digit-gold); }
  .digit-red { color: var(--digit-red); }
  .gift-tag {
    position: absolute;
    left: 623px;
    top: 661px;
    width: 363px;
    height: 89px;
    border-radius: 14px;
    background: var(--tag-cream);
    font-family: "Jost", sans-serif;
    font-weight: 400;
    font-size: 15px;
    color: var(--tag-ink);
  }
  .tag-line {
    position: absolute;
    display: flex;
    align-items: baseline;
    right: 52px;
  }
  .tag-line-to { top: 16px; left: 77px; }
  .tag-line-from { top: 56px; left: 54px; }
  .tag-rule {
    flex: 1;
    margin-left: 4px;
    border-bottom: 2px dotted var(--tag-ink);
    transform: translateY(-3px);
  }
</style>
</head>
<body>
<main class="canvas">
  <svg class="sticker" viewBox="0 0 1200 900" aria-hidden="true">
    <path class="sticker-shape" d="M505,205 A48,48 0 0 0 553,157 L600,157 Q805,40 1010,157 L1057,157 A48,48 0 0 0 1105,205 L1105,705 A95,95 0 0 0 1010,800 L600,800 A95,95 0 0 0 505,705 Z"/>
    <path class="sticker-frame" vector-effect="non-scaling-stroke" transform="translate(805 437.5) scale(.955 .96) translate(-805 -437.5)" d="M505,205 A48,48 0 0 0 553,157 L600,157 Q805,40 1010,157 L1057,157 A48,48 0 0 0 1105,205 L1105,705 A95,95 0 0 0 1010,800 L600,800 A95,95 0 0 0 505,705 Z"/>
  </svg>

  <div class="fireworks" role="img" aria-label="Colourful fireworks bursts in teal, red and gold with stars and confetti"></div>

  <p class="greeting greeting-happy">HAPPY</p>
  <p class="greeting greeting-year">NEW YEAR</p>

  <p class="year-number"><span class="digit-teal">2</span><span class="digit-coral">0</span><span class="digit-gold">1</span><span class="digit-red">7</span></p>

  <div class="gift-tag">
    <div class="tag-line tag-line-to"><span>TO</span><span class="tag-rule"></span></div>
    <div class="tag-line tag-line-from"><span>FROM</span><span class="tag-rule"></span></div>
  </div>
</main>
</body>
</html>
```